Capability statement for an Electrical Business based in Sydney Australia

The aim for the Capability statement is for us to look more professional when we meet someone or after cold calling and have to send them our business details.
Need something simple, efficient and to the point.

It should have the following content
- Our mission (details can be as attached PDF)
- Areas we service (this can be a google map of areas we service but basically the areas are
Metro Sydney with our work centralised around the Norwest, Hills, Inner west and Epping area)
- List of services we provide (as PDF)
- Details about us; who we are, contact details, licenses (as PDF)
- Why they should choose us
(As pdf)

Right now, we're just after a nice format we're happy with, the details we are happy to provide with once we have a design in mind.

I've attached our current existing capability statement and what our details are. Also, our website is
https://themardenfield.com.au/

Thanks in advance!

• Should not be complicated for the reader

```html
<!DOCTYPE html>
<html lang="en">
<head>
<meta charset="utf-8">
<title>The Marden Field – Capability Statement</title>
<link rel="stylesheet" href="https://fonts.googleapis.com/css2?family=Montserrat:ital,wght@0,400;0,500;0,600;0,700;1,400;1,700&family=Oswald:wght@600&family=Playfair+Display:wght@700;900&display=swap">
<style>
  :root{
    --red:#e0342a;
    --red-dark:#9b1410;
    --ink:#1b1b1b;
    --body:#3a3a3a;
    --white:#ffffff;
    --grey-line:#e3e3e3;
    --pill:#f1f1f1;
    --bg-top:#4a0003;
    --bg-bottom:#1b2550;
  }
  *{margin:0;padding:0;box-sizing:border-box;}
  html,body{width:1200px;height:793px;overflow:hidden;}
  body{
    position:relative;
    background:linear-gradient(180deg,var(--bg-top) 0%,#3a0a1e 45%,var(--bg-bottom) 100%);
    font-family:"Montserrat",sans-serif;
    color:var(--body);
  }
  .page{position:absolute;top:42.5px;width:546px;height:707px;background:var(--white);overflow:hidden;}
  .page--capability{left:46.5px;}
  .page--services{left:607.5px;}
  .page svg.shapes{position:absolute;left:0;top:0;}
  .abs{position:absolute;}
  .serif{font-family:"Playfair Display",serif;font-weight:700;}

  /* brand */
  .brand{position:absolute;display:flex;align-items:center;gap:6px;color:var(--red);font-family:"Montserrat",sans-serif;font-weight:700;letter-spacing:.04em;line-height:1.02;text-transform:uppercase;}
  .brand__mark{width:10px;height:10px;background:var(--red);flex:none;}
  .brand--header{left:27px;top:24px;font-size:18px;}
  .brand--header .brand__mark{width:14px;height:14px;}
  .brand--footer{font-size:13px;}

  /* hero */
  .hero-title{left:26px;top:131px;font-size:36px;line-height:50px;color:var(--white);font-weight:700;}
  .abn{right:23px;top:291px;font-size:15.5px;font-weight:600;color:var(--white);line-height:18px;}

  /* sections */
  .hex{position:absolute;width:39px;height:44px;}
  .section-title{position:absolute;left:78px;font-size:16px;line-height:18px;color:var(--ink);}
  .section-text{position:absolute;left:78px;font-size:8.3px;line-height:13.4px;color:var(--body);}
  .values{position:absolute;top:578px;font-size:8.3px;line-height:15px;color:var(--ink);list-style:none;}
  .values li{display:flex;align-items:center;gap:5px;}
  .tick{width:9px;height:9px;flex:none;}

  /* licence block */
  .licence{position:absolute;left:340px;width:162px;text-align:center;}
  .licence__title{top:339px;font-size:18px;line-height:17.5px;color:var(--red);}
  .licence__entity{position:absolute;left:364px;top:396px;width:115px;height:16px;background:var(--pill);font-size:8px;line-height:16px;text-align:center;color:var(--ink);}
  .licence__company-no{top:413px;font-size:16px;line-height:18px;font-weight:600;color:var(--ink);}
  .licence__people{top:448px;font-size:16px;line-height:19px;font-weight:500;color:var(--ink);}
  .licence__people span{color:var(--red);}
  .liability{top:508px;font-size:15px;line-height:16px;font-weight:700;font-style:italic;color:var(--ink);}
  .liability span{display:block;color:var(--red);font-weight:400;}

  /* footer */
  .contact-label{position:absolute;top:661px;font-size:8.8px;font-weight:700;color:var(--red);}
  .contact-value{position:absolute;display:flex;align-items:center;gap:6px;font-size:8.6px;font-weight:500;color:var(--ink);line-height:10px;}
  .contact-value b{font-weight:700;}
  .contact-icon{width:10px;height:10px;flex:none;}

  /* services page */
  .services-tab{left:151px;top:0;width:240px;height:45px;text-align:center;font-family:"Oswald",sans-serif;font-weight:600;font-size:30px;line-height:45px;color:var(--red);letter-spacing:.01em;}
  .services-intro{left:39px;top:60px;font-size:15.5px;line-height:20px;color:var(--white);}
  .service-list{position:absolute;top:80px;list-style:none;font-size:8.4px;line-height:19.3px;color:var(--white);}
  .service-list li{display:flex;align-items:center;gap:5px;}
  .area-map{position:absolute;left:38px;top:205px;width:469px;height:190px;background:linear-gradient(135deg,#e6ece4 0%,#dfe8dc 40%,#cfe3c9 70%,#c8dbe8 100%);}
  .why-banner{position:absolute;left:118px;top:377px;width:308px;height:35px;background:var(--white);border:2.5px solid var(--ink);text-align:center;font-size:14px;font-weight:700;line-height:30px;color:var(--red);}
  .reason-title{position:absolute;font-size:10px;line-height:12px;color:var(--ink);}
  .reason-text{position:absolute;font-size:8.2px;line-height:9.9px;color:var(--body);}
</style>
</head>
<body>

<!-- ===== Capability page ===== -->
<section class="page page--capability">
  <svg class="shapes" width="546" height="707" viewBox="0 0 546 707">
    <defs>
      <linearGradient id="houseTone" x1="0" y1="0" x2="0" y2="1">
        <stop offset="0" stop-color="#b7b6d6"/>
        <stop offset=".45" stop-color="#4b5a86"/>
        <stop offset=".75" stop-color="#8d8b86"/>
        <stop offset="1" stop-color="#5c7d3c"/>
      </linearGradient>
      <linearGradient id="redTone" x1="0" y1="0" x2="1" y2="1">
        <stop offset="0" stop-color="#b3130f"/>
        <stop offset="1" stop-color="#7a0c09"/>
      </linearGradient>
      <radialGradient id="softBlush" cx=".5" cy=".5" r=".5">
        <stop offset="0" stop-color="#fde9e9"/>
        <stop offset="1" stop-color="#ffffff"/>
      </radialGradient>
    </defs>
    <circle cx="40" cy="485" r="110" fill="url(#softBlush)"/>
    <polygon points="264,0 546,0 546,274 303,274 191,93" fill="url(#houseTone)" role="img" aria-label="Photo of a lit two-storey suburban house at dusk"/>
    <polygon points="0,93 191,93 303,274 0,274" fill="url(#redTone)" role="img" aria-label="Red-tinted photo of a house garage and driveway"/>
    <polygon points="307,274 546,274 546,315 333,315" fill="var(--red)"/>
    <!-- licence braces -->
    <path d="M348,344 Q330,344 330,362 L330,430 Q330,447 312,447 Q330,447 330,464 L330,538 Q330,556 348,556" fill="none" stroke="var(--grey-line)" stroke-width="4"/>
    <path d="M497,344 Q515,344 515,362 L515,430 Q515,447 533,447 Q515,447 515,464 L515,538 Q515,556 497,556" fill="none" stroke="var(--grey-line)" stroke-width="4"/>
    <line x1="357" y1="387" x2="484" y2="387" stroke="var(--grey-line)" stroke-width="1"/>
    <line x1="357" y1="437" x2="484" y2="437" stroke="var(--grey-line)" stroke-width="1"/>
    <!-- footer swoosh -->
    <polygon points="0,634 402,625 402,635" fill="var(--red)"/>
    <polygon points="170,640 402,636 402,644" fill="var(--ink)"/>
  </svg>

  <div class="brand brand--header"><span class="brand__mark"></span><span>The Marden<br>Field</span></div>

  <h1 class="abs serif hero-title">Capability<br>Statement</h1>
  <div class="abs abn">ABN : 58 214 907 336</div>

  <!-- Mission -->
  <svg class="hex" style="left:26px;top:301px" viewBox="0 0 39 44"><polygon points="19.5,0 39,11 39,33 19.5,44 0,33 0,11" fill="var(--red)"/><circle cx="19.5" cy="22" r="9" fill="none" stroke="#fff" stroke-width="2"/><circle cx="19.5" cy="22" r="4.5" fill="none" stroke="#fff" stroke-width="2"/><circle cx="19.5" cy="22" r="1.4" fill="#fff"/><line x1="20" y1="21.5" x2="27" y2="14.5" stroke="#fff" stroke-width="1.8"/></svg>
  <h2 class="section-title serif" style="top:298px">Our Mission</h2>
  <p class="section-text" style="top:318px">Dedicate ourselves to providing world class&nbsp; service to<br>anyone in need, based on honesty,&nbsp; communication<br>and respect.</p>

  <!-- Who we are -->
  <svg class="hex" style="left:26px;top:380px" viewBox="0 0 39 44"><polygon points="19.5,0 39,11 39,33 19.5,44 0,33 0,11" fill="var(--red)"/><polygon points="8,31 16,18 21,25 24,21 31,31" fill="#fff"/><circle cx="14" cy="14" r="2.3" fill="#fff"/><line x1="24" y1="21" x2="24" y2="11" stroke="#fff" stroke-width="1.2"/><polygon points="24,11 29,13 24,15" fill="#fff"/></svg>
  <h2 class="section-title serif" style="top:377px">Who We Are</h2>
  <p class="section-text" style="top:397px">The Marden Field is a rapidly growing Electrical<br>maintenance company that services metro<br>Sydney Areas.</p>
  <p class="section-text" style="top:450px">We are established on sound service principles with<br>honesty, communication, and respect at the<br>forefront of every team member.</p>
  <p class="section-text" style="top:496px">We strive for openness, trust, and accountability and we<br>are in the business of providing solutions to help others.<br>We see ourselves as an extension of your team.</p>

  <!-- Core values -->
  <svg class="hex" style="left:26px;top:559px" viewBox="0 0 39 44"><polygon points="19.5,0 39,11 39,33 19.5,44 0,33 0,11" fill="var(--red)"/><circle cx="19.5" cy="22" r="9" fill="none" stroke="#fff" stroke-width="2"/><circle cx="19.5" cy="22" r="4.5" fill="none" stroke="#fff" stroke-width="2"/><circle cx="19.5" cy="22" r="1.4" fill="#fff"/><line x1="20" y1="21.5" x2="27" y2="14.5" stroke="#fff" stroke-width="1.8"/></svg>
  <h2 class="section-title serif" style="top:556px">Core Values</h2>
  <ul class="values" style="left:78px">
    <li><svg class="tick" viewBox="0 0 10 10"><circle cx="5" cy="5" r="4" fill="none" stroke="var(--ink)" stroke-width="1"/><path d="M3,5 L4.6,6.6 L9,2" fill="none" stroke="var(--ink)" stroke-width="1.2"/></svg>Safety and Security is priority</li>
    <li><svg class="tick" viewBox="0 0 10 10"><circle cx="5" cy="5" r="4" fill="none" stroke="var(--ink)" stroke-width="1"/><path d="M3,5 L4.6,6.6 L9,2" fill="none" stroke="var(--ink)" stroke-width="1.2"/></svg>Support when you need it most</li>
  </ul>
  <ul class="values" style="left:245px">
    <li><svg class="tick" viewBox="0 0 10 10"><circle cx="5" cy="5" r="4" fill="none" stroke="var(--ink)" stroke-width="1"/><path d="M3,5 L4.6,6.6 L9,2" fill="none" stroke="var(--ink)" stroke-width="1.2"/></svg>Service with an over-the-top WOW</li>
    <li><svg class="tick" viewBox="0 0 10 10"><circle cx="5" cy="5" r="4" fill="none" stroke="var(--ink)" stroke-width="1"/><path d="M3,5 L4.6,6.6 L9,2" fill="none" stroke="var(--ink)" stroke-width="1.2"/></svg>Satisfaction with loyalty and integrity</li>
  </ul>

  <!-- Licence -->
  <h2 class="licence licence__title serif">Electrical<br>License Number</h2>
  <div class="licence__entity">The Marden Field Pty Ltd :</div>
  <div class="licence licence__company-no">518276C</div>
  <div class="licence licence__people">Declan : <span>204617C</span><br>Rowan : <span>391052C</span></div>
  <div class="licence liability" style="left:330px;width:182px">PUBLIC LIABILITY<span>$20,000,000</span></div>

  <!-- Footer -->
  <div class="brand brand--footer" style="left:417px;top:624px"><span class="brand__mark"></span><span>The Marden<br>Field</span></div>
  <div class="contact-label" style="left:25px">Email</div>
  <div class="contact-label" style="left:216px">Mobile Phone</div>
  <div class="contact-label" style="left:380px">Website</div>
  <div class="contact-value" style="left:27px;top:676px"><svg class="contact-icon" viewBox="0 0 10 10"><rect x=".5" y="1.5" width="9" height="7" fill="var(--red)"/><path d="M.5,1.5 L5,5.5 L9.5,1.5" fill="none" stroke="#fff" stroke-width=".8"/></svg>services@themardenfield.com.au</div>
  <div class="contact-value" style="left:216px;top:674px"><svg class="contact-icon" viewBox="0 0 10 10"><rect x="2.5" y=".5" width="5" height="9" rx="1" fill="none" stroke="var(--red)" stroke-width="1"/><circle cx="5" cy="7.8" r=".6" fill="var(--red)"/></svg><span><b>Declan :</b>&nbsp; 0400 118 274<br><b>Rowan&nbsp; :</b>&nbsp; 0400 562 930</span></div>
  <div class="contact-value" style="left:380px;top:675px"><svg class="contact-icon" viewBox="0 0 10 10"><circle cx="5" cy="5" r="4.3" fill="none" stroke="var(--red)" stroke-width="1"/><path d="M.8,5 H9.2 M5,.8 C2.5,3 2.5,7 5,9.2 M5,.8 C7.5,3 7.5,7 5,9.2" fill="none" stroke="var(--red)" stroke-width=".7"/></svg>www.themardenfield.com.au</div>
</section>

<!-- ===== Services page ===== -->
<section class="page page--services">
  <svg class="shapes" width="546" height="707" viewBox="0 0 546 707">
    <polygon points="0,0 546,0 546,246 0,362" fill="var(--red)"/>
    <polygon points="0,362 546,246 546,280 0,396" fill="var(--ink)"/>
    <polygon points="151,0 391,0 371,45 168,45" fill="var(--white)"/>
    <rect x="33" y="200" width="479" height="200" rx="3" fill="var(--ink)"/>
  </svg>

  <div class="abs services-tab">SERVICES</div>
  <h2 class="abs serif services-intro">Brief List of the most common services we provide</h2>

  <ul class="service-list" style="left:38px">
    <li><svg class="tick" viewBox="0 0 10 10"><circle cx="5" cy="5" r="4" fill="none" stroke="#fff" stroke-width="1"/><path d="M3,5 L4.6,6.6 L9,2" fill="none" stroke="#fff" stroke-width="1.2"/></svg>Switchboard repairs and upgrade</li>
    <li><svg class="tick" viewBox="0 0 10 10"><circle cx="5" cy="5" r="4" fill="none" stroke="#fff" stroke-width="1"/><path d="M3,5 L4.6,6.6 L9,2" fill="none" stroke="#fff" stroke-width="1.2"/></svg>Lighting installations</li>
    <li><svg class="tick" viewBox="0 0 10 10"><circle cx="5" cy="5" r="4" fill="none" stroke="#fff" stroke-width="1"/><path d="M3,5 L4.6,6.6 L9,2" fill="none" stroke="#fff" stroke-width="1.2"/></svg>Powerpoint installations</li>
    <li><svg class="tick" viewBox="0 0 10 10"><circle cx="5" cy="5" r="4" fill="none" stroke="#fff" stroke-width="1"/><path d="M3,5 L4.6,6.6 L9,2" fill="none" stroke="#fff" stroke-width="1.2"/></svg>Surge protection services</li>
    <li><svg class="tick" viewBox="0 0 10 10"><circle cx="5" cy="5" r="4" fill="none" stroke="#fff" stroke-width="1"/><path d="M3,5 L4.6,6.6 L9,2" fill="none" stroke="#fff" stroke-width="1.2"/></svg>Hot water system service and repair</li>
    <li><svg class="tick" viewBox="0 0 10 10"><circle cx="5" cy="5" r="4" fill="none" stroke="#fff" stroke-width="1"/><path d="M3,5 L4.6,6.6 L9,2" fill="none" stroke="#fff" stroke-width="1.2"/></svg>24/7 Emergency service</li>
  </ul>
  <ul class="service-list" style="left:259px">
    <li><svg class="tick" viewBox="0 0 10 10"><circle cx="5" cy="5" r="4" fill="none" stroke="#fff" stroke-width="1"/><path d="M3,5 L4.6,6.6 L9,2" fill="none" stroke="#fff" stroke-width="1.2"/></svg>Smoke Alarm installation and certifications</li>
    <li><svg class="tick" viewBox="0 0 10 10"><circle cx="5" cy="5" r="4" fill="none" stroke="#fff" stroke-width="1"/><path d="M3,5 L4.6,6.6 L9,2" fill="none" stroke="#fff" stroke-width="1.2"/></svg>Electric Vehicle charging stations</li>
    <li><svg class="tick" viewBox="0 0 10 10"><circle cx="5" cy="5" r="4" fill="none" stroke="#fff" stroke-width="1"/><path d="M3,5 L4.6,6.6 L9,2" fill="none" stroke="#fff" stroke-width="1.2"/></svg>Ceiling, exhaust fan ventilation solutions</li>
    <li><svg class="tick" viewBox="0 0 10 10"><circle cx="5" cy="5" r="4" fill="none" stroke="#fff" stroke-width="1"/><path d="M3,5 L4.6,6.6 L9,2" fill="none" stroke="#fff" stroke-width="1.2"/></svg>Appliance installations</li>
    <li><svg class="tick" viewBox="0 0 10 10"><circle cx="5" cy="5" r="4" fill="none" stroke="#fff" stroke-width="1"/><path d="M3,5 L4.6,6.6 L9,2" fill="none" stroke="#fff" stroke-width="1.2"/></svg>Fault finding</li>
    <li><svg class="tick" viewBox="0 0 10 10"><circle cx="5" cy="5" r="4" fill="none" stroke="#fff" stroke-width="1"/><path d="M3,5 L4.6,6.6 L9,2" fill="none" stroke="#fff" stroke-width="1.2"/></svg>TV, DATA and FREE TO AIR Aerial installations</li>
  </ul>

  <div class="area-map" role="img" aria-label="Map of metro Sydney service areas with numbered markers around Norwest, the Hills, Epping and the Inner West"></div>
  <div class="why-banner">WHY CHOOSE THE MARDEN FIELD ?</div>

  <!-- Reasons -->
  <svg class="hex" style="left:19px;top:433px;width:33px;height:37px" viewBox="0 0 39 44"><polygon points="19.5,0 39,11 39,33 19.5,44 0,33 0,11" fill="var(--red)"/><circle cx="19.5" cy="20" r="8" fill="none" stroke="#fff" stroke-width="2"/><path d="M11,22 V27 M28,22 V27 M25,29 Q22,32 19.5,31" fill="none" stroke="#fff" stroke-width="2"/></svg>
  <h3 class="reason-title serif" style="left:61px;top:435px">Support when you need it most</h3>
  <p class="reason-text" style="left:61px;top:452px">The Field provides around the clock assistance,<br>whether during normal business hours or<br>emergencies. We are focused on providing<br>solutions for our clients.</p>

  <svg class="hex" style="left:280px;top:433px;width:33px;height:37px" viewBox="0 0 39 44"><polygon points="19.5,0 39,11 39,33 19.5,44 0,33 0,11" fill="var(--red)"/><rect x="13" y="20" width="13" height="13" fill="#fff"/><path d="M10,15 l1.5,-3 1.5,3 M18,11 l1.5,-3 1.5,3 M26,15 l1.5,-3 1.5,3" fill="none" stroke="#fff" stroke-width="1.6"/></svg>
  <h3 class="reason-title serif" style="left:322px;top:435px">Satisfaction with loyalty and integrity</h3>
  <p class="reason-text" style="left:322px;top:452px">We value our transparency and communication<br>skills to deliver an outstanding performance<br>which reflects our happy customer base.</p>

  <svg class="hex" style="left:19px;top:507px;width:33px;height:37px" viewBox="0 0 39 44"><polygon points="19.5,0 39,11 39,33 19.5,44 0,33 0,11" fill="var(--red)"/><rect x="12" y="11" width="15" height="21" fill="none" stroke="#fff" stroke-width="2"/><path d="M15,17 H24 M15,21 H24 M15,25 H20" stroke="#fff" stroke-width="1.6"/></svg>
  <h3 class="reason-title serif" style="left:61px;top:507px">Licensed and insured technicians</h3>
  <p class="reason-text" style="left:61px;top:524px">All our technicians are experts of their field, with<br>the relevant equipment, knowledge and licenses<br>to carry out our duties</p>

  <svg class="hex" style="left:280px;top:507px;width:33px;height:37px" viewBox="0 0 39 44"><polygon points="19.5,0 39,11 39,33 19.5,44 0,33 0,11" fill="var(--red)"/><path d="M13,13 Q11,15 12,19 Q15,27 23,31 Q27,32 28,29 L25,26 L22,27 Q17,24 16,20 L17,17 Z" fill="#fff"/></svg>
  <h3 class="reason-title serif" style="left:322px;top:509px">We provide courtesy calls</h3>
  <p class="reason-text" style="left:322px;top:526px">The appointment will be confirmed the day<br>before and our technicians will call you half an<br>hour in advance on approach to the job</p>

  <svg class="hex" style="left:19px;top:572px;width:33px;height:37px" viewBox="0 0 39 44"><polygon points="19.5,0 39,11 39,33 19.5,44 0,33 0,11" fill="var(--red)"/><circle cx="19.5" cy="17" r="4" fill="#fff"/><circle cx="11.5" cy="19" r="3" fill="#fff"/><circle cx="27.5" cy="19" r="3" fill="#fff"/><path d="M12,30 Q12,22 19.5,22 Q27,22 27,30 Z M6,29 Q6,23 11.5,23 L13,24 Q10,26 10,29 Z M33,29 Q33,23 27.5,23 L26,24 Q29,26 29,29 Z" fill="#fff"/></svg>
  <h3 class="reason-title serif" style="left:61px;top:574px">Fast and responsive team with a direct contact</h3>
  <p class="reason-text" style="left:61px;top:590px">The Field treats every one of our clients as a VIP. We pride ourselves on being able to provide a quick turn around<br>for all our jobs. We make the whole process smooth, from booking the job to attending and completion.</p>

  <!-- Footer -->
  <svg class="shapes" width="546" height="707" viewBox="0 0 546 707" style="pointer-events:none">
    <polygon points="0,634 413,625 413,635" fill="var(--red)"/>
    <polygon points="170,640 413,636 413,644" fill="var(--ink)"/>
  </svg>
  <div class="brand brand--footer" style="left:428px;top:624px"><span class="brand__mark"></span><span>The Marden<br>Field</span></div>
  <div class="contact-label" style="left:36px">Email</div>
  <div class="contact-label" style="left:227px">Mobile Phone</div>
  <div class="contact-label" style="left:392px">Website</div>
  <div class="contact-value" style="left:38px;top:676px"><svg class="contact-icon" viewBox="0 0 10 10"><rect x=".5" y="1.5" width="9" height="7" fill="var(--red)"/><path d="M.5,1.5 L5,5.5 L9.5,1.5" fill="none" stroke="#fff" stroke-width=".8"/></svg>services@themardenfield.com.au</div>
  <div class="contact-value" style="left:227px;top:674px"><svg class="contact-icon" viewBox="0 0 10 10"><rect x="2.5" y=".5" width="5" height="9" rx="1" fill="none" stroke="var(--red)" stroke-width="1"/><circle cx="5" cy="7.8" r=".6" fill="var(--red)"/></svg><span><b>Declan :</b>&nbsp; 0400 118 274<br><b>Rowan&nbsp; :</b>&nbsp; 0400 562 930</span></div>
  <div class="contact-value" style="left:392px;top:675px"><svg class="contact-icon" viewBox="0 0 10 10"><circle cx="5" cy="5" r="4.3" fill="none" stroke="var(--red)" stroke-width="1"/><path d="M.8,5 H9.2 M5,.8 C2.5,3 2.5,7 5,9.2 M5,.8 C7.5,3 7.5,7 5,9.2" fill="none" stroke="var(--red)" stroke-width=".7"/></svg>www.themardenfield.com.au</div>
</section>

</body>
</html>
```